Business Card Design

My company is a Consulting & Training company (Halvorn Consulting and Training, LLC) specializing in Firearms Training, State of Florida Concealed Weapons Permit Course, and Tactical Equipment Consulting.

Industry/Entity Type

Business

Contact Information for Business Card

Tobin Halvorn
P.O. Box 412763
Aventura, FL 33197
(786)555-0148

```html
<!DOCTYPE html>
<html lang="en">
<head>
<meta charset="utf-8">
<title>Halvorn Consulting and Training – Business Card</title>
<link rel="stylesheet" href="https://fonts.googleapis.com/css2?family=Source+Sans+3:wght@400;600;700&display=swap">
<style>
  :root {
    --backdrop: #121212;
    --card: #e9ebea;
    --brand-blue: #4a8fe3;
    --ink-grey: #8b908f;
    --mark-grey: #939897;
  }
  * { margin: 0; padding: 0; box-sizing: border-box; }
  html, body {
    width: 1200px;
    height: 900px;
    overflow: hidden;
    background: var(--backdrop);
  }
  .canvas {
    position: relative;
    width: 1200px;
    height: 900px;
    font-family: "Source Sans 3", "Myriad Pro", sans-serif;
  }
  .card {
    position: absolute;
    top: 312px;
    width: 428px;
    height: 247px;
    background: var(--card);
    border-radius: 12px;
  }
  .card--front { left: 155px; }
  .card--back { left: 633px; }

  /* Front side */
  .brand-lockup {
    position: absolute;
    left: 28px;
    top: 100px;
    display: flex;
    align-items: center;
    gap: 10px;
  }
  .brand-dot {
    width: 14px;
    height: 14px;
    border-radius: 50%;
    background: var(--mark-grey);
  }
  .brand-name {
    font-size: 38px;
    font-weight: 700;
    color: var(--brand-blue);
    line-height: 1;
  }
  .contact {
    position: absolute;
    left: 229px;
    top: 56px;
    color: var(--ink-grey);
    font-size: 13px;
    line-height: 14px;
  }
  .contact__name {
    font-size: 19px;
    font-weight: 600;
    color: var(--brand-blue);
    line-height: 22px;
  }
  .contact__title { margin-bottom: 12px; }
  .contact__address { margin-bottom: 12px; }
  .contact__line {
    display: flex;
    align-items: center;
    gap: 6px;
    height: 16px;
  }
  .contact__icon {
    width: 10px;
    height: 10px;
    fill: var(--brand-blue);
    stroke: var(--brand-blue);
  }

  /* Back side */
  .back-lockup {
    position: absolute;
    inset: 0;
    display: flex;
    flex-direction: column;
    align-items: center;
    justify-content: center;
    gap: 14px;
  }
  .back-lockup .brand-dot {
    width: 18px;
    height: 18px;
  }
  .back-lockup .brand-name {
    font-size: 54px;
    letter-spacing: 2px;
    text-transform: uppercase;
  }
</style>
</head>
<body>
<main class="canvas">

  <section class="card card--front" aria-label="Business card front">
    <div class="brand-lockup">
      <span class="brand-dot"></span>
      <span class="brand-name">Halvorn</span>
    </div>

    <div class="contact">
      <p class="contact__name">Tobin Halvorn</p>
      <p class="contact__title">Managing Director</p>
      <p class="contact__address">P.O. Box 412763<br>Aventura, FL 33197</p>
      <p class="contact__line">
        <svg class="contact__icon" viewBox="0 0 10 10" aria-hidden="true"><path stroke="none" d="M1 3.2C1 2 3 1.6 5 1.6s4 .4 4 1.6v.8H7V3.2H3V4H1z M2.5 5 L3.4 4.2h3.2L7.5 5 8.5 8.4H1.5z"/></svg>
        (786)555-0148
      </p>
      <p class="contact__line">
        <svg class="contact__icon" viewBox="0 0 10 10" aria-hidden="true"><rect stroke="none" x="1" y="2.5" width="8" height="5.5" rx=".5"/><path fill="none" stroke="#e9ebea" stroke-width=".8" d="M1.3 3 5 5.8 8.7 3"/></svg>
        info@halvorntraining.com
      </p>
      <p class="contact__line">
        <svg class="contact__icon" viewBox="0 0 10 10" aria-hidden="true"><g fill="none" stroke-width="1.2"><rect x="1" y="4.5" width="5" height="2.6" rx="1.3" transform="rotate(-45 3.5 5.8)"/><rect x="4" y="2.8" width="5" height="2.6" rx="1.3" transform="rotate(-45 6.5 4.1)"/></g></svg>
        www.halvorntraining.com
      </p>
    </div>
  </section>

  <section class="card card--back" aria-label="Business card back">
    <div class="back-lockup">
      <span class="brand-dot"></span>
      <span class="brand-name">Halvorn</span>
    </div>
  </section>

</main>
</body>
</html>
```